Professional, Elegant, Modern and Playful stationery design for an Orthodontist (Dentist)

We need a new stationery design for an Orthodontist (Dentist).
We would like to see designs that are elegant, but also playful. The designs and colors should be in harmony with the existing logo (uploaded).
The font of the logo text is roboto (Google), you don't need to use the same font, but the used font has to be in harmony with the font used in the logo and it has to be usable in Microsoft Word.
The colors used have to be in harmony with the logo.
The design for following parts are needed:
- A4 letter paper design
- A4 Microsoft Word Template (with and without letterhead)
- Envelope designs for C4 and C5 with the window on the right side
- CD/DVD-label design
- Stamping design

Target Market(s)

Orthodontist (Dentist)

Industry/Entity Type

It Professional

Font styles to use
Sans Serif

Colors

Designer to choose colors to be used in the design.

Requirements
Must have
• * Logo files are uploaded
• * A4 letter paper design: for printing press
• - Address position is on the right side
• - Needed Information in the letterhead:
• - Logo with company name as a unit
• or
• - separate the logo from the text and position them separately
• - Text needed:
• Kieferorthopädie Wendelau
• Dr. med. dent. Lukas Brenner
• Fachzahnarzt für Kieferorthopädie (CH)
• Eidg. dipl. Zahnarzt, Mitglied VZB und FDT
• Hagelbachweg 14
• 8907 Schlieren
• 044 512 37 90
• (fax:)
• 044 512 37 91
• info@wendelau-praxis.net
• www.wendelau-praxis.net
• * A4 Microsoft Word Templates:
• - an empty and undesigned text example template is uploaded
• - the address lines are already correctly positioned behind the envelope window
• - design the positions of all elements
• - choose suitable fonts, which are in harmony with the font in the logo and the letterhead and which can be used in Microsoft Word (compatible with latest version, no old versions (.doc) needed)
• - choose suitable font sizes weights and colors, which are in harmony with the font in the logo and the letterhead.
• - One version with letterhead for printing on an empty paper
• - One version without letterhead for printing on a paper with letterhead already printed in printing press
• * Envelopes C4 and C5
• - window on the right side
• - Logo with company name (see uploaded files) as a unit
• or
• - Text needed:
• Hagelbachweg 14
• 8907 Schlieren
• * DVD/CD-label:
• or
• - Text needed:
• Hagelbachweg 14
• 8907 Schlieren
• 044 512 37 90
• info@wendelau-praxis.net
• www.wendelau-praxis.net
• - Patient name with birth date:
• Doe John, *1.2.1999
• - Two lines of text describing the contents on the CD/DVD
• * Stamping design:
• - Logo
• - Text:
• Kieferorthopädie Wendelau GmbH
• Hagelbachweg 14
• 8907 Schlieren
Nice to have
• -
Should not have
• - Old Microsoft Word versions (.doc)

```html
<!DOCTYPE html>
<html lang="de">
<head>
<meta charset="utf-8">
<title>Kieferorthopädie Wendelau – Stationery</title>
<link href="https://fonts.googleapis.com/css2?family=Roboto:wght@400;500;700&display=swap" rel="stylesheet">
<style>
  :root{
    --navy:#1b1f7a;
    --blue:#0aa3e3;
    --indigo:#2f3fa0;
    --grey-text:#6b6b6b;
    --ink:#333;
    --line:#5a5a5a;
    --paper:#ffffff;
    --stage:#eceef0;
  }
  *{box-sizing:border-box;margin:0;padding:0}
  html,body{width:1200px;height:938px;overflow:hidden}
  body{background:var(--stage);position:relative;font-family:'Roboto',sans-serif;color:var(--ink)}
  .sheet{position:absolute;background:var(--paper);overflow:hidden;border:1px solid #e1e3e6}
  .band{position:absolute;left:0;bottom:0;width:100%}
  .brand{position:absolute;display:flex;align-items:center}
  .brand-dot{border-radius:50%;background:var(--blue);flex:none}
  .brand-name{color:var(--navy);font-weight:700;white-space:nowrap}
  .brand-sub{color:var(--grey-text);font-weight:400;white-space:nowrap}
  .url{position:absolute;color:#fff;letter-spacing:.2em;font-weight:500;white-space:nowrap}

  /* letterhead */
  .letterhead{left:184px;top:68px;width:386px;height:544px}
  .letterhead .brand{left:22px;top:27px;gap:7px}
  .letterhead .brand-dot{width:20px;height:20px}
  .letterhead .brand-name{font-size:7px}
  .letterhead .brand-sub{font-size:5px;line-height:1.3}
  .contact{position:absolute;text-align:right;font-size:4.6px;line-height:2;color:#222;white-space:nowrap}
  .letterhead .contact{right:17px;top:22px}
  .letter-body{position:absolute;left:37px;top:138px;width:295px;font-size:5.2px;line-height:1.6;color:#333}
  .letter-body p{margin-bottom:8px}
  .letter-body .gap{margin-bottom:22px}
  .signature{width:40px;height:22px;background:linear-gradient(90deg,#e6e6e6,#f4f4f4);margin:10px 0 10px}
  .bold{font-weight:700}

  /* folder */
  .folder{left:637px;top:42px;width:457px;height:574px}
  .folder .brand{left:56px;top:252px;gap:26px}
  .folder .brand-dot{width:58px;height:58px}
  .folder .brand-name{font-size:19px;margin-bottom:3px}
  .folder .brand-sub{font-size:13.5px;line-height:1.3;letter-spacing:.02em}
  .folder .url{left:22px;bottom:10px;font-size:10px}

  /* business cards */
  .card{width:175px;height:98px;border-radius:7px}
  .card-front{left:46px;top:660px}
  .card-back{left:46px;top:786px;height:99px}
  .card .brand{left:13px;top:12px;gap:6px}
  .card .brand-dot{width:14px;height:14px}
  .card .brand-name{font-size:5.6px}
  .card .brand-sub{font-size:4px;line-height:1.3}
  .card-back .brand{left:28px;top:36px;gap:8px}
  .card-back .brand-dot{width:20px;height:20px}
  .card-back .brand-name{font-size:6.6px}
  .card-back .brand-sub{font-size:4.8px}
  .holder{position:absolute;left:103px;top:24px;font-size:5.2px;color:#222;line-height:1.3}
  .holder .role{font-size:4.2px}
  .card .contact{left:103px;top:37px;text-align:left;font-size:3.4px;line-height:1.8}
  .card-address{position:absolute;left:10px;bottom:6px;color:#fff;font-size:4.6px;line-height:1.6;letter-spacing:.04em}

  /* envelopes */
  .envelope-front{left:266px;top:674px;width:432px;height:207px}
  .envelope-front .brand{left:20px;top:22px;gap:8px}
  .envelope-front .brand-dot{width:22px;height:22px}
  .envelope-front .brand-name{font-size:6.8px}
  .envelope-front .brand-sub{font-size:4.8px;line-height:1.3}
  .envelope-front .url{left:14px;bottom:9px;font-size:8px}
  .envelope-back{left:737px;top:672px;width:432px;height:207px}
  .flap{position:absolute;left:0;top:0;width:100%;height:72px;border-radius:0 0 38px 38px;background:linear-gradient(90deg,var(--indigo),var(--blue) 60%,var(--indigo))}
  .flap .url{left:0;right:0;top:29px;text-align:center;font-size:10px}
</style>
</head>
<body>

<svg width="0" height="0" style="position:absolute" aria-hidden="true">
  <defs>
    <linearGradient id="bandFill" x1="0" y1="0" x2="1" y2="0">
      <stop offset="0" stop-color="#2f3fa0"/>
      <stop offset=".6" stop-color="#0aa3e3"/>
      <stop offset="1" stop-color="#2f3fa0"/>
    </linearGradient>
    <symbol id="band" viewBox="0 0 400 100" preserveAspectRatio="none">
      <path d="M0,28 C130,4 260,56 400,12" fill="none" stroke="#5a5a5a" stroke-width="3"/>
      <path d="M0,45 C130,20 260,72 400,28 L400,100 L0,100 Z" fill="url(#bandFill)"/>
    </symbol>
  </defs>
</svg>

<!-- A4 letterhead -->
<section class="sheet letterhead">
  <div class="brand">
    <span class="brand-dot"></span>
    <div>
      <div class="brand-name">Kieferorthopädie Wendelau</div>
      <div class="brand-sub">Dr. med. dent. Lukas Brenner<br>Fachzahnarzt für Kieferorthopädie (CH)</div>
    </div>
  </div>
  <div class="contact">
    Hagelbachweg 14<br>8907 Schlieren<br>044 512 37 90 ☏<br>079 418 22 63 ▯<br>044 512 37 91 ▤<br>info@wendelau-praxis.net ✉<br>www.wendelau-praxis.net ◍
  </div>
  <div class="letter-body">
    <p>2. Juli 2012</p>
    <p><span class="bold">Dear CH,</span><br>Seeweg 5, 8000 Zürich</p>
    <p class="gap">Lorem ipsum dolor sit amet, consectetur adipiscing elit, sed do eiusmod tempor incididunt ut labore et dolore magna aliqua. Ut enim ad minim veniam, quis nostrud exercitation ullamco laboris nisi ut aliquip ex ea commodo consequat. Duis aute irure dolor in reprehenderit in voluptate velit esse cillum dolore eu fugiat nulla pariatur. Excepteur sint occaecat cupidatat non proident, sunt in culpa qui officia deserunt mollit anim id est laborum. Sed ut perspiciatis unde omnis iste natus error sit voluptatem.</p>
    <p class="gap">Lorem ipsum dolor sit amet, consectetur adipiscing elit, sed do eiusmod tempor incididunt ut labore et dolore magna aliqua. Ut enim ad minim veniam, quis nostrud exercitation ullamco laboris.</p>
    <p>Lorem ipsum dolor sit amet, consectetur adipiscing elit, sed do eiusmod tempor incididunt ut labore et dolore magna aliqua. Ut enim ad minim veniam, quis nostrud exercitation ullamco laboris nisi ut aliquip ex ea commodo consequat. Duis aute irure dolor in reprehenderit in voluptate velit esse cillum dolore eu fugiat nulla pariatur. Excepteur sint occaecat cupidatat non proident, sunt in culpa qui officia deserunt mollit anim id est laborum. Sed ut perspiciatis unde omnis iste natus error sit voluptatem.</p>
    <p>Best Regards,</p>
    <div class="signature" role="img" aria-label="Handwritten signature"></div>
    <p><span class="bold">Daniel Roth</span><br>Director</p>
    <p>Seeweg 5, 8000 Zürich</p>
  </div>
  <svg class="band" height="92"><use href="#band"/></svg>
</section>

<!-- Presentation folder -->
<section class="sheet folder">
  <div class="brand">
    <span class="brand-dot"></span>
    <div>
      <div class="brand-name">Kieferorthopädie Wendelau</div>
      <div class="brand-sub">Dr. med. dent. Lukas Brenner<br>Fachzahnarzt für Kieferorthopädie (CH)</div>
    </div>
  </div>
  <svg class="band" height="100"><use href="#band"/></svg>
  <div class="url">www.wendelau-praxis.net</div>
</section>

<!-- Business card front -->
<section class="sheet card card-front">
  <div class="brand">
    <span class="brand-dot"></span>
    <div>
      <div class="brand-name">Kieferorthopädie Wendelau</div>
      <div class="brand-sub">Dr. med. dent. Lukas Brenner<br>Fachzahnarzt für Kieferorthopädie (CH)</div>
    </div>
  </div>
  <div class="holder">PETER HOLZ<br><span class="role">Managing Director</span></div>
  <div class="contact">☏ 044 512 37 90<br>▯ 079 418 22 63<br>▤ 044 512 37 91<br>✉ info@wendelau-praxis.net<br>◍ www.wendelau-praxis.net</div>
  <svg class="band" height="30"><use href="#band"/></svg>
  <div class="card-address">Hagelbachweg 14<br>8907 Schlieren</div>
</section>

<!-- Business card back -->
<section class="sheet card card-back">
  <div class="brand">
    <span class="brand-dot"></span>
    <div>
      <div class="brand-name">Kieferorthopädie Wendelau</div>
      <div class="brand-sub">Dr. med. dent. Lukas Brenner<br>Fachzahnarzt für Kieferorthopädie (CH)</div>
    </div>
  </div>
</section>

<!-- Envelope front -->
<section class="sheet envelope-front">
  <div class="brand">
    <span class="brand-dot"></span>
    <div>
      <div class="brand-name">Kieferorthopädie Wendelau</div>
      <div class="brand-sub">Dr. med. dent. Lukas Brenner<br>Fachzahnarzt für Kieferorthopädie (CH)</div>
    </div>
  </div>
  <svg class="band" height="66"><use href="#band"/></svg>
  <div class="url">www.wendelau-praxis.net</div>
</section>

<!-- Envelope back -->
<section class="sheet envelope-back">
  <div class="flap"><div class="url">www.wendelau-praxis.net</div></div>
</section>

</body>
</html>
```